Brava-Lux.ch is looking for business card letterhead and envelope C5 with WOW effect

We need a strong business card for our company Brava-Lux.ch, logo is available. You want a black or dark background on which the logo Stark r% 26 # 252; appears. Letterhead and envelope in C5 format should be in a similar design, but does not have to be We need a strong business card for our company Brava-Lux.ch, logo is available. A black or dark background is desired, on which the logo Stark comes across. The letterhead and the envelope in C5 format should have a similar design.

Target Market(s)

Private customers as well as entrepreneurs

Contact Information for Business Card

E-mail: info@brava-lux.ch
Web.www.Brava-Lux.ch
Tel: +41 ( 0 ) 79 384 6027
Adresse:
Kellerweg 14
9405 Ostheim

Hier kann man Icons verwenden für Email,Tel und Adressse

Font styles to use
Other font styles liked:
• Dubai,bold

Colors

Designer to choose colors to be used in the design.

Requirements
Must have
• WOW effect
Nice to have
• R% 26 # 252; back business card with our service listings. - VEHICLE LABELING - SHOP WINDOW LABELING - STICKERS AND MUCH MORE ... in red color

```html
<!DOCTYPE html>
<html lang="en">
<head>
<meta charset="utf-8">
<title>Brava-Lux.ch Stationery</title>
<link href="https://fonts.googleapis.com/css2?family=Quicksand:wght@400;500;700&family=Arimo:wght@400;700&display=swap" rel="stylesheet">
<style>
:root{
  --bg:#e6e6e6;
  --paper:#f2f2f2;
  --ink:#151515;
  --grey:#7a7a7a;
  --text-grey:#8c8c8c;
  --yellow:#f0b51c;
  --dark-1:#262626;
  --dark-2:#141414;
  --dark-logo:#6e6e6e;
}
*{margin:0;padding:0;box-sizing:border-box}
html,body{width:1200px;height:2845px;overflow:hidden;background:var(--bg)}
body{position:relative;font-family:'Quicksand',sans-serif;color:var(--grey)}
.sheet{position:absolute;left:227px;width:745px;background:var(--paper)}
.card-front{top:127px;height:426px}
.card-back{top:632px;height:427px;background:radial-gradient(ellipse at 55% 45%,var(--dark-1),var(--dark-2))}
.letterhead{top:1164px;left:225px;width:747px;height:941px}
.envelope{top:2182px;left:225px;width:747px;height:529px}
.abs{position:absolute}
.brand{position:absolute;display:flex;align-items:center;gap:14px;font-family:'Quicksand',sans-serif;font-weight:700;color:var(--ink);letter-spacing:.5px;white-space:nowrap}
.brand .dot{border-radius:50%;background:var(--yellow);flex:none}
.card-front .brand{left:42px;top:180px;font-size:36px}
.card-front .brand .dot{width:44px;height:44px}
.card-back .brand{left:165px;top:183px;font-size:40px;color:var(--dark-logo)}
.card-back .brand .dot{width:48px;height:48px;background:#0c0c0c}
.letterhead .brand,.envelope .brand{left:30px;top:62px;font-size:26px;gap:12px}
.letterhead .brand .dot,.envelope .brand .dot{width:34px;height:34px}
.person-name{left:474px;top:86px;font-size:23px;font-weight:700;color:var(--yellow);letter-spacing:1.5px}
.person-title{left:474px;top:112px;font-size:20px;letter-spacing:1px}
.rule{position:absolute;right:0;height:2px;background:var(--yellow)}
.card-front .rule{left:474px;top:167px}
.address{position:absolute;letter-spacing:1px;line-height:1.2}
.card-front .address{left:474px;top:197px;font-size:20px}
.contacts{position:absolute;list-style:none;letter-spacing:1px}
.contacts li{display:flex;align-items:center;white-space:nowrap}
.contacts svg{flex:none}
.contacts .hl{color:var(--yellow);font-weight:700}
.card-front .contacts{left:474px;top:262px;font-size:20px}
.card-front .contacts li{height:24.5px;gap:12px}
.small .contacts li{height:15.5px;gap:8px}
.letterhead .address{left:568px;top:28px;font-size:13px}
.letterhead .rule{left:568px;top:70px}
.letterhead .contacts{left:568px;top:84px;font-size:13px}
.envelope .address{left:38px;top:396px;font-size:13px}
.envelope .rule{left:38px;top:437px}
.envelope .contacts{left:38px;top:449px;font-size:13px}
.network{position:absolute;inset:0;background:linear-gradient(180deg,rgba(255,255,255,0) 20%,rgba(255,255,255,.05) 55%,rgba(255,255,255,0))}
.letter{font-family:'Arimo',sans-serif;color:var(--text-grey)}
.meta-label{font-size:12.5px;font-weight:700;color:var(--ink)}
.meta-value{font-size:12px;margin-top:2px}
.subject{left:223px;top:290px}
.date{left:618px;top:288px}
.salutation{left:223px;top:379px;font-size:16px;font-weight:700;color:#888}
.body{left:223px;top:416px;width:457px;font-size:12px;line-height:15.8px;text-align:justify}
.body p+p{margin-top:15.8px}
.sidenote{left:40px;top:456px;width:127px;text-align:right;font-size:12px;line-height:15.5px}
.sidenote .lead{color:var(--ink)}
.sidenote p+p{margin-top:8px}
.signature{left:223px;top:758px;font-size:16px;line-height:19px;color:#888}
</style>
</head>
<body>

<svg width="0" height="0" style="position:absolute">
  <defs>
    <symbol id="ico-phone" viewBox="0 0 16 16"><circle cx="8" cy="8" r="8" fill="#f0b51c"/><path d="M4.5 6.5c0-1 1-1.8 3.5-1.8s3.5.8 3.5 1.8l-1.2.4-.5-1H6.2l-.5 1zM6 7.5h4l1 3.5H5z" fill="#fff"/></symbol>
    <symbol id="ico-mail" viewBox="0 0 16 16"><circle cx="8" cy="8" r="8" fill="#f0b51c"/><rect x="4" y="5" width="8" height="6" rx="1" fill="none" stroke="#fff" stroke-width="1.2"/><path d="M4.3 5.5 8 8.3l3.7-2.8" fill="none" stroke="#fff" stroke-width="1.1"/></symbol>
    <symbol id="ico-web" viewBox="0 0 16 16"><circle cx="8" cy="8" r="8" fill="#f0b51c"/><circle cx="8" cy="8" r="4.2" fill="none" stroke="#fff" stroke-width="1.2"/><path d="M3.8 8h8.4M8 3.8c-2 2.8-2 5.6 0 8.4M8 3.8c2 2.8 2 5.6 0 8.4" fill="none" stroke="#fff" stroke-width=".9"/></symbol>
  </defs>
</svg>

<!-- Business card front -->
<section class="sheet card-front">
  <div class="brand"><span class="dot"></span>BRAVA-LUX.CH</div>
  <div class="abs person-name">LUKAS BRENNER</div>
  <div class="abs person-title">Managing Director</div>
  <div class="rule"></div>
  <div class="address">Kellerweg 14<br>9405 Ostheim</div>
  <ul class="contacts">
    <li><svg width="17" height="17"><use href="#ico-phone"/></svg>+41 ( 0 ) 79 384 6027</li>
    <li><svg width="17" height="17"><use href="#ico-mail"/></svg>info@brava-lux.ch</li>
    <li><svg width="17" height="17"><use href="#ico-web"/></svg><span>www.<span class="hl">Brava-Lux</span>.ch</span></li>
  </ul>
</section>

<!-- Business card back -->
<section class="sheet card-back">
  <div class="network" role="img" aria-label="Faint connected-dot network pattern across the dark background"></div>
  <div class="brand"><span class="dot"></span>BRAVA-LUX.CH</div>
</section>

<!-- Letterhead -->
<section class="sheet letterhead small">
  <div class="brand"><span class="dot"></span>BRAVA-LUX.CH</div>
  <div class="address">Kellerweg 14<br>9405 Ostheim</div>
  <div class="rule"></div>
  <ul class="contacts">
    <li><svg width="12" height="12"><use href="#ico-phone"/></svg>+41 ( 0 ) 79 384 6027</li>
    <li><svg width="12" height="12"><use href="#ico-mail"/></svg>info@brava-lux.ch</li>
    <li><svg width="12" height="12"><use href="#ico-web"/></svg><span>www.<span class="hl">Brava-Lux</span>.ch</span></li>
  </ul>

  <div class="letter">
    <div class="abs subject"><div class="meta-label">SUBJECT :</div><div class="meta-value">Lorem Ipsum is simply dummy</div></div>
    <div class="abs date"><div class="meta-label">DATE :</div><div class="meta-value">15-09-2017</div></div>
    <div class="abs salutation">Dear Person,</div>
    <div class="abs body">
      <p>Lorem Ipsum is simply dummy text of the printing and typesetting industry. Lorem Ipsum has been the industry's standard dummy text ever since the 1500s, when an unknown printer took a galley of type and scrambled it to make a type specimen book. It has survived not only five centuries, but also the leap into electronic typesetting, remaining essentially unchanged. It was popularised in the 1960s with the release of Vellaset sheets containing Lorem Ipsum passages, and more recently with desktop publishing software like Quill Layout including versions of Lorem Ipsum.</p>
      <p>Lorem Ipsum is simply dummy text of the printing and typesetting industry. Lorem Ipsum has been the industry's standard dummy text ever since the 1500s, when an unknown printer took a galley of type and scrambled it to make a type specimen book. It has survived not only five centuries, but also the leap into electronic typesetting, remaining essentially unchanged. It was popularised in the 1960s with the release of</p>
      <p>Vellaset sheets containing Lorem Ipsum passages, and more recently with desktop publishing software like Quill Layout including versions of Lorem Ipsum.lease of Vellaset sheets containing Lorem Ipsum passages, and more recently with desktop publishing software like Quill Layout including versions of Lorem Ipsum. publishing software like Quill Layout including versions of Lorem Ipsum.</p>
    </div>
    <div class="abs sidenote">
      <p><span class="lead">Lorem Ipsum is</span><br>simply dummy text<br>of the printing</p>
      <p><span class="lead">Lorem Ipsum is</span><br>simply dummy text</p>
    </div>
    <div class="abs signature">Lukas Brenner<br>Managing Director</div>
  </div>
</section>

<!-- Envelope C5 -->
<section class="sheet envelope small">
  <div class="brand"><span class="dot"></span>BRAVA-LUX.CH</div>
  <div class="address">Kellerweg 14<br>9405 Ostheim</div>
  <div class="rule"></div>
  <ul class="contacts">
    <li><svg width="12" height="12"><use href="#ico-phone"/></svg>+41 ( 0 ) 79 384 6027</li>
    <li><svg width="12" height="12"><use href="#ico-mail"/></svg>info@brava-lux.ch</li>
    <li><svg width="12" height="12"><use href="#ico-web"/></svg><span>www.<span class="hl">Brava-Lux</span>.ch</span></li>
  </ul>
</section>

</body>
</html>
```